I need a label design to go on our jars of honey. Our company is called Quillbrook Honey Co. The type of honey is called Marram Glade Honey. The jars are 1kg. Attached is the label size. Left hand side needs to have nutritional info... as attached. Middle section is our company name, honey type, 1kg & Whangamata, NZ. Right hand side needs to have info as per photo (raw honey etc). I would like to upload more pictures... but I’m unsure how to do this? Thanks, Noreen

Target Market(s)

Honey consumers... families

Industry/Entity Type

Food Production

Colors

Designer to choose colors to be used in the design.

Requirements
Must have
• Nutritional info as per upload
• Type of honey & company name as per upload
• 1kg
• Address
Nice to have
• Similar fonts to upload.
• Possibly background image... floral or beach... very faint though.

```html
<!DOCTYPE html>
<html lang="en">
<head>
<meta charset="utf-8">
<title>Quillbrook Honey Co. – Marram Glade Honey label</title>
<link href="https://fonts.googleapis.com/css2?family=Amatic+SC:wght@400;700&family=Open+Sans:wght@400;600;700&family=Patrick+Hand&family=Yellowtail&display=swap" rel="stylesheet">
<style>
  :root {
    --label-red: #d25a5e;
    --label-red-deep: #c84e55;
    --label-red-glow: #de7379;
    --ink: #ffffff;
  }
  html, body {
    margin: 0;
    padding: 0;
    width: 1200px;
    height: 605px;
    overflow: hidden;
    background: var(--label-red);
  }
  .label {
    position: relative;
    width: 1200px;
    height: 605px;
    color: var(--ink);
    overflow: hidden;
  }
  .label__pattern {
    position: absolute;
    inset: 0;
    background:
      radial-gradient(ellipse at 50% 48%, var(--label-red-glow) 0%, var(--label-red) 45%, var(--label-red-deep) 100%);
  }

  /* Left panel */
  .facts {
    position: absolute;
    left: 44px;
    top: 52px;
    width: 244px;
    font-family: "Open Sans", sans-serif;
    font-weight: 600;
    text-align: center;
  }
  .facts__claim {
    font-size: 16px;
    line-height: 20px;
    margin: 0 0 12px;
  }
  .nutrition {
    border: 1.5px solid var(--ink);
    font-size: 11px;
    text-align: left;
  }
  .nutrition__title {
    font-size: 15px;
    font-weight: 600;
    padding: 4px 6px 3px;
    border-bottom: 1.5px solid var(--ink);
    letter-spacing: 0.2px;
  }
  .nutrition__serves {
    padding: 5px 6px 6px;
    font-size: 11.5px;
    line-height: 15px;
    font-weight: 700;
    border-bottom: 1.5px solid var(--ink);
  }
  .nutrition table {
    width: 100%;
    border-collapse: collapse;
    font-weight: 700;
  }
  .nutrition th {
    font-size: 9.5px;
    font-weight: 600;
    text-align: left;
    padding: 5px 6px;
    border-bottom: 3px solid var(--ink);
  }
  .nutrition td {
    padding: 1px 6px;
    line-height: 18px;
    font-size: 11.5px;
  }
  .nutrition tbody tr:first-child td { padding-top: 6px; }
  .nutrition tbody tr:last-child td { padding-bottom: 6px; }
  .facts__storage {
    margin: 20px 0 0;
    font-size: 15px;
    line-height: 20px;
  }
  .batch {
    margin-top: 18px;
    border: 1.5px solid var(--ink);
    text-align: left;
    font-size: 14.5px;
    line-height: 20px;
    padding: 8px 10px 10px;
    height: 60px;
  }

  /* Centre panel */
  .brand {
    position: absolute;
    left: 380px;
    width: 440px;
    text-align: center;
  }
  .brand__company {
    top: 62px;
    margin: 0;
    font-family: "Amatic SC", sans-serif;
    font-weight: 400;
    font-size: 58px;
    line-height: 62px;
    letter-spacing: 11px;
  }
  .brand__honey {
    top: 248px;
    margin: 0;
    font-family: "Yellowtail", cursive;
    font-weight: 400;
    font-size: 66px;
    line-height: 74px;
  }
  .brand__weight {
    top: 478px;
    font-family: "Amatic SC", sans-serif;
    font-size: 34px;
    line-height: 40px;
  }
  .brand__origin {
    top: 522px;
    font-family: "Amatic SC", sans-serif;
    font-size: 40px;
    line-height: 44px;
    letter-spacing: 1px;
  }

  /* Right panel */
  .story {
    position: absolute;
    left: 900px;
    top: 72px;
    width: 260px;
    text-align: center;
    font-family: "Patrick Hand", cursive;
    font-size: 18px;
    line-height: 21.5px;
  }
  .story p { margin: 0 0 25px; }
  .story .story__thanks { margin-top: 61px; }
  .story address {
    font-style: normal;
    margin-top: 60px;
  }
</style>
</head>
<body>
<main class="label">
  <div class="label__pattern" role="img" aria-label="Faint floral pattern of tropical flowers and leaves across the label"></div>

  <section class="facts">
    <p class="facts__claim">100% New Zeland Honey<br>No added ingredients</p>
    <div class="nutrition">
      <div class="nutrition__title">NUTRITIONAL INFORMATION</div>
      <div class="nutrition__serves">Servings per package: 100<br>Serving size: 10g</div>
      <table>
        <thead>
          <tr><th>Average Quantity</th><th>per Serving</th><th>per 100g</th></tr>
        </thead>
        <tbody>
          <tr><td>Energy</td><td>134kj</td><td>1340kj</td></tr>
          <tr><td>Protein</td><td>0.04g</td><td>0.4g</td></tr>
          <tr><td>Fat total</td><td>0g</td><td>0g</td></tr>
          <tr><td>&nbsp;- saturated</td><td>0g</td><td>0g</td></tr>
          <tr><td>Carbohydrate</td><td>7.9g</td><td>79g</td></tr>
          <tr><td>&nbsp;- sugars</td><td>7.8g</td><td>78.1g</td></tr>
          <tr><td>Sodium</td><td>1.2mg</td><td>12mg</td></tr>
        </tbody>
      </table>
    </div>
    <p class="facts__storage">Store upright in a cool, dry place.<br>No refrigeration needed.<br>Not recomended for infants<br>below the age of 12 months.</p>
    <div class="batch">Best before:<br>RMP:<br>Batch No:</div>
  </section>

  <h1 class="brand brand__company">QUILLBROOK<br>HONEY CO.</h1>
  <h2 class="brand brand__honey">Marram Glade<br>Honey</h2>
  <div class="brand brand__weight">1kg</div>
  <div class="brand brand__origin">Whangamata, NZ</div>

  <section class="story">
    <p>Sourced from the beautiful<br>Coromandel Pensinula.</p>
    <p>Our honey comes to you raw &amp;<br>unpasterurised, ensured it retains<br>all the natural goodness!</p>
    <p>Arohanui,<br>Rowan, Noreen &amp; boys</p>
    <p class="story__thanks">'Quillbrook' - all thanks to God for<br>His incredible creation!</p>
    <address>www.quillbrookhoney.co.nz<br>24 Tidewater Rd<br>Whangamata<br>New Zeland</address>
  </section>
</main>
</body>
</html>
```